TovaLamishpacha - Israeli Mental Health Website

We are developing an Israeli website for mental health. The website will be both in English and in Hebrew. We have a logo and would like a website design based on the logo and the logos colors (attached).

Attached is a doc that contains the website requirements.

We would like to have an icon for each of the sidebar categories, an image for each of the pages (including each of the sidebar category pages).

Target Market(s)

Adults 18-80

Industry/Entity Type

Mental Health

Number of Pages Required

5+ page

Font styles to use
Sans Serif

Colors

Designer to choose colors to be used in the design.

```html
<!DOCTYPE html>
<html lang="en">
<head>
<meta charset="utf-8">
<title>TovaLamishpacha - Organization for Mental Health</title>
<link href="https://fonts.googleapis.com/css2?family=Catamaran:wght@400;500;600;700;800&family=Roboto:wght@400;500&display=swap" rel="stylesheet">
<style>
:root{
  --blue:#2172bf;
  --blue-light:#4a86c8;
  --green:#54ab3f;
  --ink:#1b1b1b;
  --text:#333;
  --gray-bg:#f3f3f3;
  --white:#fff;
}
*{box-sizing:border-box;margin:0;padding:0}
html,body{width:1200px;height:2388px;overflow:hidden}
body{position:relative;font-family:"Catamaran",sans-serif;color:var(--text);background:var(--white)}

/* header */
.site-header{position:absolute;left:0;top:0;width:1200px;height:118px}
.brand{position:absolute;left:146px;top:40px;display:flex;align-items:center;gap:8px;font-weight:700;font-size:22px;color:var(--blue)}
.brand-dot{width:14px;height:14px;border-radius:50%;background:var(--green)}
.call{position:absolute;left:621px;top:28px;font-size:17px;font-weight:600;color:var(--blue-light)}
.lang{position:absolute;left:762px;top:28px;font-family:"Roboto",sans-serif;font-size:16px;color:#333}
.search{position:absolute;left:880px;top:18px;width:194px;height:37px;border:1px solid #bbb;font-family:"Roboto",sans-serif;font-size:14px;color:#888;padding:9px 15px}
.search svg{position:absolute;right:12px;top:11px}
.nav-band{position:absolute;left:0;top:71px;width:1200px;height:47px}
.nav{position:absolute;left:433px;top:84px;display:flex;gap:29px;font-family:"Roboto",sans-serif;font-size:16px;color:var(--white)}

/* hero */
.hero{position:absolute;left:0;top:118px;width:1200px;height:601px;background:linear-gradient(100deg,#b9c3c4 0%,#cfd3d0 35%,#8a7664 55%,#d8d2ca 80%,#ece7e2 100%)}
.hero-photo{position:absolute;inset:0}
.hero-title{position:absolute;left:244px;top:210px;width:410px;text-align:center;font-weight:700;font-size:50px;line-height:58px;color:var(--white)}
.btn{position:absolute;display:flex;align-items:center;justify-content:center;color:var(--white);font-weight:700;font-size:16px;border-radius:4px}
.btn-hero{left:364px;top:346px;width:159px;height:49px;background:var(--blue)}
.side-menu{position:absolute;left:24px;top:119px;width:202px;height:567px;background:var(--green);border-radius:6px}
.side-item{position:absolute;left:12px;font-weight:700;font-size:13px;line-height:17px;color:var(--white)}
.side-icon{position:absolute;left:188px;width:28px;height:28px;border-radius:50%;border:2px solid var(--white);background:var(--green);display:flex;align-items:center;justify-content:center}
.side-icon svg{width:16px;height:16px;fill:none;stroke:var(--white);stroke-width:1.8;stroke-linecap:round;stroke-linejoin:round}

/* about */
.about-photo{position:absolute;left:144px;top:805px;width:426px;height:426px;border-radius:50%;background:linear-gradient(135deg,#a9b9c0,#8d5048 65%,#6b3934)}
.about-title{position:absolute;left:640px;top:818px;font-weight:800;font-size:38px;color:var(--ink);letter-spacing:.5px}
.about-text{position:absolute;left:636px;top:879px;width:452px;font-family:"Roboto",sans-serif;font-size:15px;line-height:25.7px;color:#333}
.btn-about{left:632px;top:1182px;width:159px;height:49px;background:var(--green)}

/* services */
.services{position:absolute;left:0;top:1354px;width:1200px;height:954px;background:var(--gray-bg)}
.card{position:absolute;background:var(--white);border-radius:8px;box-shadow:0 1px 4px rgba(0,0,0,.06);text-align:center}
.card-img{margin:10px;height:202px;border-radius:6px}
.card h3{font-weight:600;font-size:16px;color:var(--ink);margin-top:16px;letter-spacing:.3px}
.card p{font-size:12.5px;line-height:21px;color:#333;padding:0 20px;margin-top:6px}
.card a{display:inline-block;margin-top:8px;font-weight:700;font-size:11px;color:var(--green);text-decoration:underline}

/* footer */
.site-footer{position:absolute;left:0;top:2308px;width:1200px;height:80px;background:var(--blue)}
.foot-copy{position:absolute;left:110px;top:27px;font-size:16px;color:var(--white)}
.foot-link{position:absolute;top:27px;font-size:16px;color:var(--green);text-decoration:underline}
.chat-float{position:absolute;left:1126px;top:2277px;width:50px;height:50px;border-radius:50%;background:var(--white);box-shadow:0 2px 6px rgba(0,0,0,.15)}
</style>
</head>
<body>

<header class="site-header">
  <div class="brand"><span class="brand-dot"></span>TovaLamishpacha</div>
  <div class="call">Call Us Today</div>
  <div class="lang">EN <svg width="10" height="8" viewBox="0 0 10 8"><path d="M1 2l4 4 4-4" stroke="#333" stroke-width="2" fill="none"/></svg></div>
  <div class="search">Search
    <svg width="14" height="14" viewBox="0 0 14 14"><circle cx="6" cy="6" r="4.5" stroke="#111" stroke-width="2" fill="none"/><path d="M9.5 9.5l3.5 3.5" stroke="#111" stroke-width="2.4"/></svg>
  </div>
  <svg class="nav-band" width="1200" height="47" viewBox="0 0 1200 47">
    <polygon points="407,0 1200,0 1200,47 373,47" fill="var(--blue)"/>
    <rect x="0" y="44" width="380" height="3" fill="var(--blue)"/>
  </svg>
  <nav class="nav"><span>Smart ChatLine</span><span>Therapists</span><span>Organizations</span><span>Videos</span><span>Contact</span><span>About</span><span>Donate</span></nav>
</header>

<section class="hero">
  <div class="hero-photo" role="img" aria-label="Smiling woman in a bright room holding hands with a counsellor"></div>
  <h1 class="hero-title">Welcome to TovaLamishpacha</h1>
  <div class="btn btn-hero">GET STARTED</div>
</section>

<aside class="side-menu">
  <div class="side-item" style="top:17px">Emergency Mental Help</div>
  <div class="side-icon" style="top:13px"><svg viewBox="0 0 24 24"><path d="M4 5h16v11H9l-5 4z"/><path d="M12 8v3M12 13.5v.5"/></svg></div>
  <div class="side-item" style="top:59px">Suicide</div>
  <div class="side-icon" style="top:56px"><svg viewBox="0 0 24 24"><path d="M12 20s-7-4.5-7-10a4 4 0 0 1 7-2.5A4 4 0 0 1 19 10c0 5.5-7 10-7 10z"/></svg></div>
  <div class="side-item" style="top:95px">Sexual Assault<br>/Violence Victims</div>
  <div class="side-icon" style="top:99px"><svg viewBox="0 0 24 24"><path d="M12 3l7 3v5c0 5-3.5 8-7 10-3.5-2-7-5-7-10V6z"/></svg></div>
  <div class="side-item" style="top:140px">Sexual Assault<br>/Violence Assaulters</div>
  <div class="side-icon" style="top:141px"><svg viewBox="0 0 24 24"><circle cx="12" cy="12" r="8"/><path d="M6.5 6.5l11 11"/></svg></div>
  <div class="side-item" style="top:191px">Post Trauma</div>
  <div class="side-icon" style="top:185px"><svg viewBox="0 0 24 24"><circle cx="12" cy="8" r="3.5"/><path d="M5 20c1-4 3.5-6 7-6s6 2 7 6"/></svg></div>
  <div class="side-item" style="top:232px">Depression</div>
  <div class="side-icon" style="top:227px"><svg viewBox="0 0 24 24"><path d="M7 17a4 4 0 0 1 0-8 5 5 0 0 1 9.5-1A4 4 0 0 1 17 17z"/><path d="M9 20v1M13 20v1"/></svg></div>
  <div class="side-item" style="top:273px">Anxiety</div>
  <div class="side-icon" style="top:268px"><svg viewBox="0 0 24 24"><path d="M3 12l3-5 3 10 3-10 3 10 3-10 3 5"/></svg></div>
  <div class="side-item" style="top:315px">Addictions</div>
  <div class="side-icon" style="top:311px"><svg viewBox="0 0 24 24"><path d="M12 3s6 7 6 11a6 6 0 0 1-12 0c0-4 6-11 6-11z"/></svg></div>
  <div class="side-item" style="top:358px">Sleep Disorders</div>
  <div class="side-icon" style="top:354px"><svg viewBox="0 0 24 24"><path d="M19 14.5A8 8 0 1 1 9.5 5a6.5 6.5 0 0 0 9.5 9.5z"/></svg></div>
  <div class="side-item" style="top:402px">Eating Disorders</div>
  <div class="side-icon" style="top:398px"><svg viewBox="0 0 24 24"><path d="M8 3v18M5 3v5a3 3 0 0 0 6 0V3M16 21V3c2 1 3 4 3 8h-3"/></svg></div>
  <div class="side-item" style="top:446px">Financial Problems</div>
  <div class="side-icon" style="top:442px"><svg viewBox="0 0 24 24"><circle cx="12" cy="12" r="8"/><path d="M14.5 9c-.5-1-1.5-1.5-2.5-1.5-1.5 0-2.5.8-2.5 2s1 1.7 2.5 2 2.5.8 2.5 2-1 2-2.5 2c-1 0-2-.5-2.5-1.5M12 6v1.5M12 16.5V18"/></svg></div>
  <div class="side-item" style="top:488px">Parenthood</div>
  <div class="side-icon" style="top:485px"><svg viewBox="0 0 24 24"><circle cx="8" cy="7" r="2.5"/><circle cx="16" cy="10" r="2"/><path d="M4 19c0-4 2-6 4-6s4 2 4 6M13 19c0-3 1.3-5 3-5s3 2 3 5"/></svg></div>
  <div class="side-item" style="top:529px">Relationship</div>
  <div class="side-icon" style="top:525px"><svg viewBox="0 0 24 24"><circle cx="9" cy="12" r="5"/><circle cx="15" cy="12" r="5"/></svg></div>
</aside>

<section class="about">
  <div class="about-photo" role="img" aria-label="Woman in a headscarf listening during a group support session"></div>
  <h2 class="about-title">ABOUT US</h2>
  <p class="about-text">Lorem ipsum dolor sit amet, consectetur adipiscing elit, sed do eiusmod tempor incididunt ut labore et dolore magna aliqua. Quis ipsum suspendisse ultrices gravida. Risus commodo viverra maecenas accumsan lacus vel facilisis. Lorem ipsum dolor sit amet, consectetur adipiscing elit, sed do eiusmod tempor incididunt ut labore et dolore magna aliqua. Quis ipsum suspendisse ultrices gravida. Risus commodo viverra maecenas accumsan lacus vel facilisis. Lorem ipsum dolor sit amet, consectetur adipiscing elit, sed do eiusmod tempor incididunt ut labore et dolore magna aliqua. Quis ipsum suspendisse ultrices gravida. Risus commodo viverra maecenas accumsan lacus vel facilisis.</p>
  <div class="btn btn-about">LERAN MORE</div>
</section>

<section class="services">
  <article class="card" style="left:105px;top:63px;width:323px;height:393px">
    <div class="card-img" role="img" aria-label="Distressed woman resting in a hospital bed" style="background:linear-gradient(135deg,#c9b7a6,#9fb3c9)"></div>
    <h3>EMERGENCY MENTAL HELP</h3>
    <p>Lorem ipsum dolor sit amet, consectetur adipiscing elit, sed do eiusmod tempor incididunt ut labore et dolore magna aliqua. Quis ipsum suspendisse ultrices gravida. Risus commodo viverra</p>
    <a>MORE OPTIONS FOR EMERGENCY MENTAL HELP</a>
  </article>
  <article class="card" style="left:453px;top:73px;width:313px;height:383px">
    <div class="card-img" role="img" aria-label="Hand holding a phone with a chat app in front of a laptop" style="background:linear-gradient(135deg,#2f6b66,#3b3d40 60%,#c8c5c0)"></div>
    <h3>SMART CHATLINE</h3>
    <p>Lorem ipsum dolor sit amet, consectetur adipiscing elit, sed do eiusmod tempor incididunt ut labore et dolore magna aliqua. Quis ipsum suspendisse ultrices gravida. Risus commodo viverra</p>
    <a>05X-XXXXXXX</a>
  </article>
  <article class="card" style="left:783px;top:73px;width:313px;height:383px">
    <div class="card-img" role="img" aria-label="Therapist with two clients seated in a group session" style="background:linear-gradient(135deg,#e2e0da,#6d7b85 55%,#3a3f45)"></div>
    <h3>THERAPISTS</h3>
    <p>Lorem ipsum dolor sit amet, consectetur adipiscing elit, sed do eiusmod tempor incididunt ut labore et dolore magna aliqua. Quis ipsum suspendisse ultrices gravida. Risus commodo viverra</p>
    <a>FIND THERAPISTS</a>
  </article>
  <article class="card" style="left:278px;top:484px;width:313px;height:384px">
    <div class="card-img" role="img" aria-label="Business team shaking hands around a meeting table" style="background:linear-gradient(135deg,#6b5446,#2c2a2c 55%,#8a7a6c)"></div>
    <h3>ORGANIZATIONS</h3>
    <p>Lorem ipsum dolor sit amet, consectetur adipiscing elit, sed do eiusmod tempor incididunt ut labore et dolore magna aliqua. Quis ipsum suspendisse ultrices gravida. Risus commodo viverra</p>
    <a>FIND ORGANIZATIONS</a>
  </article>
  <article class="card" style="left:608px;top:484px;width:313px;height:384px">
    <div class="card-img" role="img" aria-label="Counsellor taking notes while a client talks" style="background:linear-gradient(135deg,#d8d3cc,#a89c92 55%,#5e4a40)"></div>
    <h3>VIDEOS</h3>
    <p>Lorem ipsum dolor sit amet, consectetur adipiscing elit, sed do eiusmod tempor incididunt ut labore et dolore magna aliqua. Quis ipsum suspendisse ultrices gravida. Risus commodo viverra</p>
    <a>VIDEO LIBRARY</a>
  </article>
</section>

<div class="chat-float">
  <svg width="50" height="50" viewBox="0 0 50 50">
    <circle cx="25" cy="25" r="16" fill="var(--green)"/>
    <path d="M19 18c1-1 2-1 3 0l2 3c.5 1 0 1.6-.7 2.3 1 2 2.4 3.4 4.4 4.4.7-.7 1.3-1.2 2.3-.7l3 2c1 1 1 2 0 3-2 2-5 1.5-9-2.5s-6.5-7.5-5-11.5z" fill="#fff"/>
  </svg>
</div>

<footer class="site-footer">
  <div class="foot-copy">TovaLamishpacha - Organization for Mental Health ©2023</div>
  <a class="foot-link" style="left:860px">Privacy Policy</a>
  <a class="foot-link" style="left:1051px">Terms</a>
</footer>

</body>
</html>
```